Re-design of veterinary clinic website *

For a future relaunch of our webpage, we would like to find a fresh design that still incorporates the spirit of our current one which can be found at http://dr-wenzlaff.de
We are a small business that appeals to locals but are known in a wide area for specialist services.
According to analytics data, most people rarely read through the full website but are using it to inform themselves about opening hours, Telephone numbers and location. Still, the website needs to offer enough content to be ranked positively by the Quandle algorithm.
Our logo is not part of the re-design but needs to be included in your proposal as is. It can be used a source of inspiration, just as the current design. Keep in mind, that the design will be used as the basis of a fluid webdesign for both mobile and desktop. Roughly 75% of our users are on mobile devices.
Target Market(s)
Locals
Industry/Entity Type
Veterinary
Number of Pages Required
1 page
Look and feel
Each slider illustrates characteristics of the customer's brand and the style your logo design should communicate.

```html
<!DOCTYPE html>
<html lang="de">
<head>
<meta charset="utf-8">
<title>Tierarztpraxis Dr. Jonas Wenzlaff</title>
<link href="https://fonts.googleapis.com/css2?family=Montserrat:wght@400;500;600;700&display=swap" rel="stylesheet">
<style>
:root{
  --blue:#0b4fa3;
  --blue-dark:#0a4796;
  --blue-band:#1a5fb4;
  --ink:#1f1f1f;
  --muted:#555;
  --grey-bg:#efefef;
  --grey-soft:#f6f6f6;
  --line:#d9d9d9;
  --white:#fff;
}
*{box-sizing:border-box;margin:0;padding:0}
html,body{width:715px;height:1200px;overflow:hidden;background:var(--white)}
body{font-family:'Montserrat',Arial,sans-serif;color:var(--ink)}
.page{position:relative;width:715px;height:1200px;overflow:hidden}
.abs{position:absolute}
a{color:inherit;text-decoration:none}

/* header */
.brand{left:64px;top:16px;display:flex;align-items:center;gap:8px}
.brand-mark{width:22px;height:22px;border-radius:50%;background:var(--blue)}
.brand-name{font-size:15px;font-weight:600;color:var(--blue);letter-spacing:1px}
.call{left:534px;top:16px;display:flex;align-items:center;gap:8px}
.call-text{font-size:9px;line-height:11px;color:var(--ink)}
.call-text strong{display:block;color:var(--blue);font-weight:700}

.nav{left:0;top:58px;width:715px;height:24px;background:var(--blue)}
.nav a{position:absolute;top:8px;font-size:7px;font-weight:700;color:var(--white);letter-spacing:.2px}

/* hero */
.hero{left:0;top:82px;width:715px;height:218px;background:var(--grey-bg)}
.hero-title{left:65px;top:124px;font-size:24px;font-weight:400;color:var(--blue)}
.hero-sub{left:65px;top:161px;font-size:9px;color:var(--ink)}
.btn{left:65px;top:187px;width:109px;height:25px;background:var(--blue);color:var(--white);font-size:9px;font-weight:500;display:flex;align-items:center;justify-content:center}
.hero-photo{left:60px;top:216px;width:596px;height:112px;background:linear-gradient(90deg,#b8a48a 0%,#d9a85a 30%,#e6b878 50%,#c98a45 65%,#3a3a3a 85%,#d9d9d9 100%);border-radius:40px 40px 4px 4px;opacity:.9}
.dots{display:flex;gap:7px}
.dots i{width:6px;height:6px;border-radius:50%;background:#ccd3dd;display:block}
.dots i.on{background:var(--blue)}

/* welcome */
.welcome-bg{left:0;top:300px;width:452px;height:254px;background:var(--white)}
.hours-bg{left:452px;top:300px;width:263px;height:254px;background:var(--grey-soft)}
.h2{font-size:18px;font-weight:400;color:var(--ink)}
.rule{width:22px;height:2px;background:var(--blue)}
.welcome-photo{left:66px;top:380px;width:188px;height:133px;background:linear-gradient(120deg,#6b4a2e,#c99a5c 55%,#e8d6b0)}
.welcome-text{left:269px;top:377px;width:148px;font-size:7.4px;line-height:15px;color:var(--ink)}
.more{font-size:7.4px;color:var(--blue);font-weight:500}

.hours{border-collapse:collapse;font-size:6.8px;background:var(--white)}
.hours th{background:var(--blue);color:var(--white);font-weight:600;text-align:left;padding:0 0 0 11px;width:57px;border-bottom:1px solid #2b66b0}
.hours td{width:55px;text-align:center;border:1px solid var(--line);color:var(--ink)}
.hours tr{height:21px}

/* facts */
.facts{left:0;top:554px;width:715px;height:144px;background:var(--blue-band)}
.facts-title{left:0;top:574px;width:715px;text-align:center;font-size:18px;color:var(--white)}
.fact{top:622px;width:150px;text-align:center;color:var(--white)}
.fact b{display:block;font-size:23px;font-weight:700;line-height:28px}
.fact span{font-size:11.5px;font-weight:500}

/* testimonials / blog */
.testi-bg{left:0;top:698px;width:358px;height:248px;background:var(--grey-soft)}
.sec-title{width:358px;text-align:center;font-size:14px;color:var(--ink)}
.sec-sub{width:358px;text-align:center;font-size:6.5px;color:var(--ink)}
.card{background:var(--white);box-shadow:0 1px 3px rgba(0,0,0,.12)}
.quote{left:54px;top:780px;width:248px;height:98px;padding:21px 22px 0;text-align:center;font-size:6.6px;line-height:12px}
.quote em{font-style:normal;color:var(--blue)}
.avatar{left:162px;top:865px;width:33px;height:33px;border-radius:50%;background:linear-gradient(135deg,#d9b99a,#8d6a4c);border:2px solid var(--white)}
.arrow{width:13px;height:13px;border:1px solid #bbb;border-radius:50%}
.blog{left:394px;top:780px;width:276px;height:98px}
.blog-photo{left:394px;top:780px;width:122px;height:98px;background:linear-gradient(135deg,#e8e8ea,#9ea3ab 60%,#3d4a5c)}
.blog-title{left:527px;top:792px;width:135px;font-size:11px;line-height:14px;color:var(--blue)}
.blog-text{left:527px;top:827px;width:135px;font-size:6.6px;line-height:10px}

/* footer */
.footer{left:0;top:946px;width:715px;height:214px;background:var(--blue-dark)}
.fcol-line{top:946px;width:1px;height:214px;background:rgba(255,255,255,.25)}
.fhead-line{left:0;top:990px;width:715px;height:1px;background:rgba(255,255,255,.25)}
.fhead{top:964px;display:flex;align-items:center;gap:6px;color:var(--white);font-size:12.5px}
.contact{left:66px;top:1002px;width:170px;color:var(--white);font-size:6.6px;line-height:10px}
.contact li{list-style:none;display:flex;gap:10px;margin-bottom:9px}
.contact svg{flex:0 0 auto;margin-top:1px}
.map{left:264px;top:1002px;width:188px;height:130px;background:linear-gradient(135deg,#eceff2,#dfe4ea 50%,#e9ece6)}
.map-link{left:267px;top:1138px;font-size:6.8px;color:var(--white)}
.footer .hours th{background:var(--blue-dark);border-bottom:1px solid #2b66b0}

.bottom{left:0;top:1160px;width:715px;height:40px;background:var(--white)}
.links{left:66px;top:1176px;display:flex;gap:10px;font-size:6.6px;color:var(--ink)}
.copy{left:290px;top:1176px;font-size:6.6px}
.social{left:586px;top:1172px;display:flex;gap:11px}
.social i{display:block;width:13px;height:13px;border-radius:50%;background:var(--blue-dark)}
</style>
</head>
<body>
<div class="page">

  <header>
    <div class="abs brand"><span class="brand-mark"></span><span class="brand-name">Dr. Jonas Wenzlaff</span></div>
    <div class="abs call">
      <svg width="21" height="21" viewBox="0 0 24 24"><circle cx="12" cy="12" r="10.5" fill="none" stroke="#0b4fa3" stroke-width="2"/><path d="M8.2 6.5l2 2.3-1.2 1.4c.8 1.8 2.1 3.1 3.9 3.9l1.4-1.2 2.3 2-1.3 2c-4.3-.2-8.3-4.2-8.5-8.5z" fill="#0b4fa3"/></svg>
      <div class="call-text">Call Us Today<strong>030 / 555 12 34</strong></div>
    </div>
    <nav class="abs nav">
      <a style="left:70px">HAUPTSEITE</a>
      <a style="left:150px">PRAXIS</a>
      <a style="left:210px">TEAM</a>
      <a style="left:266px">SPRECHZEITEN</a>
      <a style="left:354px">LEISTUNGEN</a>
      <a style="left:433px">KONTAKT / ANFAHRT</a>
    </nav>
  </header>

  <section>
    <div class="abs hero"></div>
    <h1 class="abs hero-title">The Finest In Veterinary Care</h1>
    <p class="abs hero-sub">We are dedicated to providing excellent care.</p>
    <a class="abs btn">Call to learn more</a>
    <div class="abs hero-photo" role="img" aria-label="Cats and dogs peeking over a ledge"></div>
    <div class="abs dots" style="left:340px;top:279px"><i></i><i class="on"></i><i></i></div>
  </section>

  <section>
    <div class="abs welcome-bg"></div>
    <div class="abs hours-bg"></div>
    <h2 class="abs h2" style="left:64px;top:329px">Herzlich Willkommen!</h2>
    <div class="abs rule" style="left:64px;top:359px"></div>
    <div class="abs welcome-photo" role="img" aria-label="Woman cuddling a golden retriever at sunset"></div>
    <p class="abs welcome-text">Herzlich Willkommen auf der Homepage der Tierarztpraxis von Dr. Jonas Wenzlaff. Mein Team und ich haben hier Informationen rund um die Praxis und Hinweise für Patientenbesitzer zusammengestellt.</p>
    <a class="abs more" style="left:269px;top:498px">Read more about us ›</a>
    <div class="abs dots" style="left:141px;top:530px"><i></i><i class="on"></i><i></i></div>

    <h2 class="abs h2" style="left:452px;top:327px;width:263px;text-align:center">Working Hours</h2>
    <div class="abs rule" style="left:572px;top:357px"></div>
    <table class="abs hours" style="left:494px;top:380px">
      <tr><th>Montag</th><td>9:30 - 11:00</td><td>6:00 - 19:00</td></tr>
      <tr><th>Dienstag</th><td>9:30 - 11:00</td><td>6:00 - 19:00</td></tr>
      <tr><th>Mittwoch</th><td>9:30 - 11:00</td><td>6:00 - 19:00</td></tr>
      <tr><th>Donnerstag</th><td>--</td><td>16:00 - 19:00</td></tr>
      <tr><th>Freitag</th><td>9:30 - 11:00</td><td>16:00 - 19:00</td></tr>
      <tr><th>Samstag</th><td>9:30 - 11:00</td><td>--</td></tr>
    </table>
  </section>

  <section>
    <div class="abs facts"></div>
    <h2 class="abs facts-title">Quick facts</h2>
    <div class="abs" style="left:347px;top:600px;width:22px;height:2px;background:#fff"></div>
    <div class="abs fact" style="left:95px"><b>10+</b><span>years of experience</span></div>
    <div class="abs fact" style="left:235px"><b>410+</b><span>satisfied clients</span></div>
    <div class="abs fact" style="left:361px"><b>681+</b><span>animals saved</span></div>
    <div class="abs fact" style="left:483px"><b>21+</b><span>expert doctors</span></div>
  </section>

  <section>
    <div class="abs testi-bg"></div>
    <h2 class="abs sec-title" style="left:0;top:723px">Testimonials</h2>
    <div class="abs rule" style="left:168px;top:746px"></div>
    <p class="abs sec-sub" style="left:0;top:753px">Hear what people's are saying about us?</p>
    <div class="abs arrow" style="left:20px;top:816px"></div>
    <div class="abs arrow" style="left:324px;top:816px"></div>
    <div class="abs card quote">"Dr. Jonas Wenzlaff is caring and kind towards animals. It is clear this is his passion. In addition, he explains your options and doesn't try to oversell services. I highly recommend the clinic."<br><em>- John Doe</em></div>
    <div class="abs avatar" role="img" aria-label="Client portrait"></div>
    <div class="abs dots" style="left:163px;top:919px"><i></i><i class="on"></i><i></i></div>

    <h2 class="abs sec-title" style="left:358px;top:723px">Latest Blog</h2>
    <div class="abs rule" style="left:526px;top:746px"></div>
    <p class="abs sec-sub" style="left:358px;top:753px">See whats new and infomation about us</p>
    <div class="abs arrow" style="left:373px;top:816px"></div>
    <div class="abs arrow" style="left:681px;top:816px"></div>
    <div class="abs card blog"></div>
    <div class="abs blog-photo" role="img" aria-label="Kitten being examined by a veterinarian"></div>
    <h3 class="abs blog-title" style="font-weight:400">THE BENEFITS OF PET MASSAGE</h3>
    <p class="abs blog-text">Want to ease your pet's aches and pains? Try massage! ...</p>
    <a class="abs more" style="left:527px;top:862px;font-size:6.6px">Read more ›</a>
    <div class="abs dots" style="left:521px;top:919px"><i></i><i class="on"></i><i></i></div>
  </section>

  <footer>
    <div class="abs footer"></div>
    <div class="abs fcol-line" style="left:238px"></div>
    <div class="abs fcol-line" style="left:477px"></div>
    <div class="abs fhead-line"></div>

    <div class="abs fhead" style="left:65px">
      <svg width="13" height="11" viewBox="0 0 13 11"><rect x=".6" y=".6" width="11.8" height="9.8" fill="none" stroke="#fff" stroke-width="1.2"/><rect x="2.5" y="3" width="3" height="4" fill="#fff"/><path d="M7 3.5h4M7 5.5h4M7 7.5h3" stroke="#fff"/></svg>Contact</div>
    <div class="abs fhead" style="left:264px">
      <svg width="11" height="11" viewBox="0 0 11 11"><circle cx="5.5" cy="3.3" r="2.5" fill="none" stroke="#fff" stroke-width="1.1"/><path d="M1 10.5c0-2.6 2-4 4.5-4s4.5 1.4 4.5 4z" fill="none" stroke="#fff" stroke-width="1.1"/></svg>Map</div>
    <div class="abs fhead" style="left:501px">
      <svg width="14" height="13" viewBox="0 0 14 13"><rect x=".6" y="1.6" width="10" height="9" fill="none" stroke="#fff" stroke-width="1.1"/><path d="M.6 4h10M3 .5v2.5M8 .5v2.5" stroke="#fff"/><circle cx="10.5" cy="9.5" r="3" fill="#0a4796" stroke="#fff"/></svg>Office Hours</div>

    <ul class="abs contact">
      <li><svg width="10" height="10" viewBox="0 0 10 10"><circle cx="5" cy="3" r="2.3" fill="#fff"/><path d="M.5 10c0-2.6 2-4 4.5-4s4.5 1.4 4.5 4z" fill="#fff"/></svg><span>Dr. med. vet. Jonas Wenzlaff<br><br>Fachtierarzt für Kleintiere<br>Lindenhofstrasse 4b</span></li>
      <li><svg width="10" height="12" viewBox="0 0 10 12"><path d="M5 12S.5 7 .5 4.5a4.5 4.5 0 0 1 9 0C9.5 7 5 12 5 12z" fill="#fff"/><circle cx="5" cy="4.5" r="1.6" fill="#0a4796"/></svg><span>14167 Berlin (Steglitz)</span></li>
      <li><svg width="10" height="10" viewBox="0 0 24 24"><path d="M5 3l4 4-2 3c1.5 3 3.8 5.5 7 7l3-2 4 4-3 3C10 22 2 14 2 6z" fill="#fff"/></svg><span>Telefon: 030 / 555 12 34<br>Telefax: 030 / 555 12 35</span></li>
      <li><svg width="10" height="9" viewBox="0 0 10 9"><rect x=".5" y="2" width="9" height="6.5" fill="#fff"/><circle cx="5" cy="5.2" r="1.8" fill="#0a4796"/><rect x="3" y=".5" width="4" height="2" fill="#fff"/></svg><span>Auch Nachts, an Wochenenden sowie an Feiertagen versuchen wir in dringenden Notfällen unter unserer Praxishandynummer 0170 555 019 0 für Sie erreichbar zu sein.</span></li>
    </ul>

    <div class="abs map" role="img" aria-label="Street map showing the practice location"></div>
    <a class="abs map-link">Locate us on Quandle Map</a>

    <table class="abs hours" style="left:501px;top:1004px">
      <tr><th>Montag</th><td>9:30 - 11:00</td><td>6:00 - 19:00</td></tr>
      <tr><th>Dienstag</th><td>9:30 - 11:00</td><td>6:00 - 19:00</td></tr>
      <tr><th>Mittwoch</th><td>9:30 - 11:00</td><td>6:00 - 19:00</td></tr>
      <tr><th>Donnerstag</th><td>--</td><td>16:00 - 19:00</td></tr>
      <tr><th>Freitag</th><td>9:30 - 11:00</td><td>16:00 - 19:00</td></tr>
      <tr><th>Samstag</th><td>9:30 - 11:00</td><td>--</td></tr>
    </table>

    <div class="abs bottom"></div>
    <nav class="abs links"><a>contact us</a><a>sitemap</a><a>privacy</a><a>terms</a></nav>
    <p class="abs copy">© 2019 dr-wenzlaff.de. All right reserved.</p>
    <div class="abs social"><i></i><i></i><i></i></div>
  </footer>

</div>
</body>
</html>
```